Technical Refinement & Corporate Adaptation of AI Graphics

We have a follow-up project for you that involves technically refining existing, AI-generated graphics and recreating them professionally in Microsoft PowerPoint. - as you did already. The content and core structure should remain unchanged, but the visual style needs to be aligned with the corporate design of the Kraftwerkhaus Morlen (colors, typography, and visual language). The primary focus is to ensure all elements are fully editable, perfectly aligned, and deliver a clean, scientific-technical look.

```html
<!DOCTYPE html>
<html lang="en">
<head>
<meta charset="utf-8">
<title>Integrated Process Assessment – Kraftwerkhaus Morlen</title>
<link href="https://fonts.googleapis.com/css2?family=Raleway:wght@400;500;600;700;800&display=swap" rel="stylesheet">
<style>
  :root{
    --green:#627d00;
    --green-dark:#4f6600;
    --green-soft:#e9edda;
    --panel-border:#e2e6d6;
    --ink:#1b1b1b;
    --ink-soft:#333;
    --grey-line:#b9b9b9;
    --opt-a:#0b35b3;
    --opt-b:#5b7b0f;
    --opt-c:#f28c00;
    --bg:#ffffff;
    --band-bg:#f6f7f1;
  }
  *{box-sizing:border-box;margin:0;padding:0}
  html,body{width:1200px;height:675px;overflow:hidden;background:var(--bg)}
  body{font-family:"Raleway",sans-serif;color:var(--ink);position:relative}
  .abs{position:absolute}

  /* header */
  .slide-number{left:33px;top:16px;width:70px;height:70px;border-radius:50%;background:#111;color:#fff;
    font-weight:800;font-size:31px;display:flex;align-items:center;justify-content:center;letter-spacing:-.5px}
  .header-rule{left:135px;top:20px;width:2px;height:64px;background:var(--green)}
  .title{left:167px;top:11px;font-size:37px;font-weight:800;color:var(--green);letter-spacing:-.2px;line-height:1.2}
  .subtitle{left:167px;top:58px;font-size:22px;font-weight:700;color:var(--ink);line-height:1.2}
  .brand{right:22px;top:22px;display:flex;align-items:center;gap:9px}
  .brand-dot{width:34px;height:34px;border-radius:50%;border:2px solid var(--green)}
  .brand-name{font-size:21px;font-weight:800;color:var(--green);line-height:1}

  /* panels */
  .panel{border:1.5px solid var(--panel-border);border-radius:10px;background:#fff}
  .dims{left:25px;top:99px;width:279px;height:284px}
  .panel-heading{font-size:17px;font-weight:700;color:var(--green)}
  .dims .panel-heading{position:absolute;left:12px;top:11px}
  .dim-row{position:absolute;left:7px;width:265px;height:52px;border:1.5px solid var(--panel-border);border-radius:5px;display:flex;overflow:hidden}
  .dim-icon{width:86px;background:var(--green-soft);display:flex;align-items:center;justify-content:center}
  .dim-icon svg{width:34px;height:34px;fill:var(--green)}
  .dim-label{padding-left:10px;display:flex;align-items:center;font-weight:700;font-size:13px;line-height:1.2}

  .chart{left:313px;top:99px;width:493px;height:284px}
  .chart svg{position:absolute;left:0;top:0}

  .insights{left:819px;top:99px;width:361px;height:284px}
  .insight{position:absolute;left:38px;display:flex;align-items:center;gap:16px}
  .insight-icon{width:56px;height:56px;border-radius:50%;background:var(--green-soft);display:flex;align-items:center;justify-content:center;flex:none}
  .insight-icon svg{width:34px;height:34px;stroke:var(--green);fill:none;stroke-width:1.6}
  .insight p{font-size:13.5px;line-height:1.35;color:var(--ink-soft)}

  /* bands */
  .band{left:25px;width:1155px;border:1.5px solid var(--panel-border);border-radius:10px;overflow:hidden}
  .band-head{background:var(--green);color:#fff;font-weight:800;font-size:22px;text-align:center;height:34px;line-height:34px}
  .methods{top:393px;height:107px;background:#fff}
  .benefits{top:506px;height:125px;background:var(--band-bg)}
  .band-items{position:relative;height:calc(100% - 34px)}
  .item{position:absolute;display:flex;align-items:center;gap:10px;color:var(--green);font-size:14px;line-height:1.05;font-weight:500}
  .methods .item{top:18px}
  .methods .item svg{width:38px;height:38px;fill:var(--green);flex:none}
  .benefits .item{top:12px;gap:12px}
  .benefit-icon{width:58px;height:58px;border-radius:50%;background:var(--green-soft);display:flex;align-items:center;justify-content:center;flex:none}
  .benefit-icon svg{width:34px;height:34px;fill:var(--green)}

  /* footer */
  .page-count{left:27px;top:645px;font-weight:700;font-size:12.5px;color:var(--green)}
  .progress{left:88px;top:655px;width:170px;height:1px;background:var(--grey-line)}
  .progress span{display:block;width:43px;height:2px;margin-top:-.5px;background:var(--green)}
  .tagline{left:274px;top:644px;font-size:14px;color:var(--ink)}
  .footer-rule{left:938px;top:655px;width:43px;height:1px;background:var(--grey-line)}
  .url{right:21px;top:644px;font-size:14px;color:var(--green)}
</style>
</head>
<body>

<svg width="0" height="0" style="position:absolute" aria-hidden="true">
  <symbol id="i-leaf" viewBox="0 0 40 40"><path d="M6 36c2-14 10-24 24-26-1 14-9 23-21 24l-3 2zm6-5c4-6 9-11 15-15-7 3-12 8-15 15z"/><circle cx="33" cy="8" r="2.5"/><circle cx="36" cy="3" r="1.6"/></symbol>
  <symbol id="i-bars" viewBox="0 0 40 40"><rect x="4" y="24" width="8" height="12"/><rect x="16" y="14" width="8" height="22"/><rect x="28" y="4" width="8" height="32"/></symbol>
  <symbol id="i-people" viewBox="0 0 40 40"><circle cx="20" cy="11" r="6"/><path d="M9 33c0-8 5-13 11-13s11 5 11 13z"/><circle cx="8" cy="15" r="4.5"/><path d="M0 33c0-6 3-10 8-10 2 0 3 .5 4 1-3 2-4 6-4 9z"/><circle cx="32" cy="15" r="4.5"/><path d="M40 33c0-6-3-10-8-10-2 0-3 .5-4 1 3 2 4 6 4 9z"/></symbol>
  <symbol id="i-gear" viewBox="0 0 40 40"><path d="M17 2h6l1 5 4 2 4-3 4 4-3 4 2 4 5 1v6l-5 1-2 4 3 4-4 4-4-3-4 2-1 5h-6l-1-5-4-2-4 3-4-4 3-4-2-4-5-1v-6l5-1 2-4-3-4 4-4 4 3 4-2zm3 10a8 8 0 100 16 8 8 0 000-16z"/></symbol>
  <symbol id="i-db" viewBox="0 0 40 40"><ellipse cx="20" cy="7" rx="15" ry="5"/><path d="M5 11c0 3 7 5 15 5s15-2 15-5v6c0 3-7 5-15 5S5 20 5 17zM5 21c0 3 7 5 15 5s15-2 15-5v6c0 3-7 5-15 5S5 30 5 27zM5 31c0 3 7 5 15 5s15-2 15-5v2c0 3-7 5-15 5S5 36 5 33z"/></symbol>
  <symbol id="i-layers" viewBox="0 0 40 40"><path d="M14 4h22v22h-3V7H14z"/><path d="M9 9h22v22h-3V12H9z"/><path d="M4 14h22v22H4zm4 18h14V18c-8 2-13 7-14 14z"/></symbol>
  <symbol id="i-network" viewBox="0 0 40 40"><circle cx="20" cy="20" r="5"/><circle cx="5" cy="5" r="4"/><circle cx="35" cy="5" r="4"/><circle cx="5" cy="35" r="4"/><circle cx="35" cy="35" r="4"/><path d="M7 8l10 10-1.5 1.5-10-10zM33 8L23 18l1.5 1.5 10-10zM7 32l10-10 1.5 1.5-10 10zM33 32L23 22l-1.5 1.5 10 10z"/></symbol>
  <symbol id="i-doc" viewBox="0 0 40 40"><path d="M8 2h17l9 9v27H8zm3 3v30h20V13h-8V5z"/><circle cx="20" cy="26" r="7"/><path d="M16.5 26l2.5 2.5 5-5" stroke="#fff" stroke-width="2" fill="none"/></symbol>
  <symbol id="i-shield" viewBox="0 0 40 40"><path d="M20 2l15 6v11c0 10-7 17-15 20C12 36 5 29 5 19V8zm0 3L8 10v9c0 8 5 14 12 17 7-3 12-9 12-17v-9z"/><path d="M13 20l5 5 9-10-2-2-7 8-3-3z"/></symbol>
  <symbol id="i-search" viewBox="0 0 40 40"><path d="M16 5a12 12 0 109 20l9 9 3-3-9-9A12 12 0 0016 5zm0 3a9 9 0 110 18 9 9 0 010-18z"/><path d="M29 2l1.5 4.5L35 8l-4.5 1.5L29 14l-1.5-4.5L23 8l4.5-1.5z"/></symbol>
  <symbol id="i-bulb" viewBox="0 0 40 40"><path d="M20 8a10 10 0 00-6 18c1 1 2 3 2 5h8c0-2 1-4 2-5a10 10 0 00-6-18zM16 34h8M17 37h6M20 2v2M8 6l1.5 1.5M32 6l-1.5 1.5M4 17h2M34 17h2"/></symbol>
  <symbol id="i-target" viewBox="0 0 40 40"><circle cx="19" cy="21" r="15"/><circle cx="19" cy="21" r="10"/><circle cx="19" cy="21" r="4"/><path d="M19 21L34 6M30 4l4 2 2 4"/></symbol>
  <symbol id="i-idea" viewBox="0 0 40 40"><path d="M20 4a12 12 0 00-7 22c1 1 2 3 2 5h10c0-2 1-4 2-5a12 12 0 00-7-22zM15 34h10M16 37h8"/><ellipse cx="20" cy="16" rx="7" ry="3"/><ellipse cx="20" cy="16" rx="3" ry="7" transform="rotate(45 20 16)"/></symbol>
  <symbol id="i-cog" viewBox="0 0 40 40"><path d="M17 3h6l1 4 4 2 4-2 4 4-2 4 2 4 4 1v6l-4 1-2 4 2 4-4 4-4-2-4 2-1 4h-6l-1-4-4-2-4 2-4-4 2-4-2-4-4-1v-6l4-1 2-4-2-4 4-4 4 2 4-2z"/><circle cx="20" cy="20" r="9"/></symbol>
</svg>

<!-- header -->
<div class="abs slide-number">01</div>
<div class="abs header-rule"></div>
<h1 class="abs title">Integrated Process Assessment</h1>
<h2 class="abs subtitle">for Technology and Product Innovation</h2>
<div class="abs brand"><span class="brand-dot"></span><span class="brand-name">Kraftwerkhaus Morlen</span></div>

<!-- assessment dimensions -->
<section class="abs panel dims">
  <h3 class="panel-heading">Assessment Dimensions</h3>
  <div class="dim-row" style="top:37px"><div class="dim-icon"><svg><use href="#i-leaf"/></svg></div><div class="dim-label">Environmental<br>(LCA)</div></div>
  <div class="dim-row" style="top:98px"><div class="dim-icon"><svg><use href="#i-bars"/></svg></div><div class="dim-label">Economic<br>(TEA)</div></div>
  <div class="dim-row" style="top:158px"><div class="dim-icon"><svg><use href="#i-people"/></svg></div><div class="dim-label">Social<br>(S-LCA)</div></div>
  <div class="dim-row" style="top:219px"><div class="dim-icon"><svg><use href="#i-gear"/></svg></div><div class="dim-label">Technical<br>Performance</div></div>
</section>

<!-- radar chart -->
<section class="abs panel chart">
  <svg width="493" height="284" viewBox="500 158 788 454" font-family="Raleway, sans-serif">
    <text x="895" y="200" text-anchor="middle" font-size="27" font-weight="700" fill="#627d00">Overall Sustainability Performance</text>
    <text x="895" y="229" text-anchor="middle" font-size="22" font-weight="700" fill="#627d00">(Normalized)</text>
    <g stroke="#b9b9b9" stroke-width="2.5">
      <line x1="827" y1="435" x2="827" y2="290"/><line x1="827" y1="435" x2="965" y2="390"/>
      <line x1="827" y1="435" x2="912" y2="552"/><line x1="827" y1="435" x2="742" y2="552"/>
      <line x1="827" y1="435" x2="689" y2="390"/>
    </g>
    <polygon points="827,395 865,423 851,467 803,467 789,423" fill="none" stroke="#627d00" stroke-width="1.2"/>
    <polygon points="827,290 965,390 912,552 742,552 689,390" fill="none" stroke="#0b35b3" stroke-width="3"/>
    <polygon points="827,321 935,400 894,527 760,527 719,400" fill="none" stroke="#5b7b0f" stroke-width="3"/>
    <polygon points="827,352 906,409 876,502 778,502 748,409" fill="none" stroke="#f28c00" stroke-width="3"/>
    <g fill="#0b35b3"><circle cx="827" cy="290" r="5"/><circle cx="965" cy="390" r="5"/><circle cx="912" cy="552" r="5"/><circle cx="742" cy="552" r="5"/><circle cx="689" cy="390" r="5"/></g>
    <g fill="#5b7b0f"><circle cx="827" cy="321" r="5"/><circle cx="935" cy="400" r="5"/><circle cx="894" cy="527" r="5"/><circle cx="760" cy="527" r="5"/><circle cx="719" cy="400" r="5"/></g>
    <g fill="#f28c00"><circle cx="827" cy="352" r="4.5"/><circle cx="906" cy="409" r="4.5"/><circle cx="876" cy="502" r="4.5"/><circle cx="778" cy="502" r="4.5"/><circle cx="748" cy="409" r="4.5"/></g>
    <g font-size="23" fill="#1b1b1b" text-anchor="middle">
      <text x="829" y="270">Safety</text>
      <text x="1010" y="395">Cost</text>
      <text x="608" y="373">Social</text><text x="608" y="394">Acceptance</text>
      <text x="659" y="565">Technology</text><text x="659" y="586">Performance</text>
      <text x="980" y="573">Resource</text><text x="980" y="594">Use</text>
    </g>
    <g font-size="16" stroke-width="2">
      <line x1="1114" y1="318" x2="1151" y2="318" stroke="#0b35b3"/><circle cx="1132" cy="318" r="5" fill="#fff" stroke="#0b35b3"/><text x="1161" y="324" fill="#0b35b3" stroke="none">Option A</text>
      <line x1="1114" y1="352" x2="1151" y2="352" stroke="#5b7b0f"/><circle cx="1132" cy="352" r="5" fill="#fff" stroke="#5b7b0f"/><text x="1161" y="358" fill="#5b7b0f" stroke="none">Option B</text>
      <line x1="1114" y1="386" x2="1151" y2="386" stroke="#f28c00"/><circle cx="1132" cy="386" r="5" fill="#fff" stroke="#f28c00"/><text x="1161" y="392" fill="#f28c00" stroke="none">Option C</text>
    </g>
    <rect x="1080" y="470" width="183" height="106" rx="4" fill="#fff" stroke="#dfe4cf" stroke-width="1.5"/>
    <path d="M1084 470h175a4 4 0 014 4v30h-183v-30a4 4 0 014-4z" fill="#627d00"/>
    <text x="1171" y="495" text-anchor="middle" font-size="17" font-weight="700" fill="#fff">KEY FINDINGS</text>
    <g font-size="15.5" fill="#1b1b1b" text-anchor="middle">
      <text x="1171" y="526">Option B shows the</text>
      <text x="1171" y="546">best overall balance</text>
      <text x="1171" y="566">across all dimensions.</text>
    </g>
  </svg>
</section>

<!-- insights -->
<section class="abs panel insights">
  <div class="insight" style="top:19px"><div class="insight-icon"><svg><use href="#i-bulb"/></svg></div><p>Integrated assessment enables<br>robust decision-making.</p></div>
  <div class="insight" style="top:85px"><div class="insight-icon"><svg><use href="#i-target"/></svg></div><p>Identifies trade-offs across<br>dimensions.</p></div>
  <div class="insight" style="top:151px"><div class="insight-icon"><svg><use href="#i-idea"/></svg></div><p>Supports technology and<br>product innovation.</p></div>
  <div class="insight" style="top:217px"><div class="insight-icon"><svg><use href="#i-cog"/></svg></div><p>Highlights preferred options<br>for further development.</p></div>
</section>

<!-- methods & tools -->
<section class="abs band methods">
  <div class="band-head">METHODS &amp; TOOLS</div>
  <div class="band-items">
    <div class="item" style="left:15px"><svg><use href="#i-leaf"/></svg><span>Life Cycle<br>Assessment (LCA)</span></div>
    <div class="item" style="left:203px"><svg><use href="#i-db"/></svg><span>Techno-Economic<br>Analysis (TEA)</span></div>
    <div class="item" style="left:392px"><svg style="width:52px"><use href="#i-people"/></svg><span>Social Life Cycle<br>Assessment (S-LCA)</span></div>
    <div class="item" style="left:626px"><svg><use href="#i-layers"/></svg><span>Multi-criteria<br>analysis (MCDA)</span></div>
    <div class="item" style="left:805px"><svg><use href="#i-network"/></svg><span>Scenario analysis<br>and modeling</span></div>
    <div class="item" style="left:995px"><svg><use href="#i-doc"/></svg><span>Visualization &amp;<br>dashboards</span></div>
  </div>
</section>

<!-- benefits & results -->
<section class="abs band benefits">
  <div class="band-head">BENEFITS &amp; RESULTS</div>
  <div class="band-items">
    <div class="item" style="left:18px"><div class="benefit-icon"><svg><use href="#i-shield"/></svg></div><span>Holistic evaluation<br>across sustainability<br>dimensions</span></div>
    <div class="item" style="left:247px"><div class="benefit-icon"><svg><use href="#i-db"/></svg></div><span>Transparent<br>assumptions &amp;<br>comparability</span></div>
    <div class="item" style="left:465px"><div class="benefit-icon"><svg><use href="#i-search"/></svg></div><span>Identification of<br>key levers and<br>trade-offs</span></div>
    <div class="item" style="left:678px"><div class="benefit-icon"><svg><use href="#i-people"/></svg></div><span>Improved decision<br>support for policy,<br>investment and R&amp;D</span></div>
    <div class="item" style="left:917px"><div class="benefit-icon"><svg><use href="#i-leaf"/></svg></div><span>Contribution to a<br>climate-neutral and<br>resource-efficient future</span></div>
  </div>
</section>

<!-- footer -->
<div class="abs page-count">01 | 13</div>
<div class="abs progress"><span></span></div>
<div class="abs tagline">Holistic research, analysis and solutions for a secure, climate-neutral and resource-efficient future</div>
<div class="abs footer-rule"></div>
<div class="abs url">www.kraftwerkhaus-morlen.at</div>

</body>
</html>
```